Leaf Haven Business Card Design

My E-Commerce store is called Leaf Haven

Website address is - http://www.leafhaven-demo.com.au

I would like a colourful, friendly business with the description in the 'must haves' box incorporated into it
Updates

Please add the following to the business cards; Natural & Organic Products Online Organic Pantry Items Superfoods & Supplements Natural Skincare Eco Friendly Household Products

Industry/Entity Type

Business

Contact Information for Business Card

www.leafhaven-demo.com.au
mira@leafhaven-demo.com.au

Colors
acd037
9bcb3c
cadf82
eaf2ce

Requirements
Must have
• Natural & Organic Eco Products Online.
• Leaf Haven specialises in organic pantry items, superfoods and supplements, organic skincare for you and your family & eco friendly household products.

```html
<!DOCTYPE html>
<html lang="en">
<head>
<meta charset="utf-8">
<title>Leaf Haven Business Card</title>
<link rel="stylesheet" href="https://fonts.googleapis.com/css2?family=Montserrat:wght@700&family=Questrial&display=swap">
<style>
  :root {
    --backdrop: #e4eedf;
    --card-white: #f7f8f6;
    --green-deep: #17a552;
    --green-mid: #2fc26b;
    --green-light: #7ad98f;
    --text-green: #1aa552;
    --text-white: #ffffff;
  }
  html, body {
    margin: 0;
    padding: 0;
    width: 1200px;
    height: 800px;
    overflow: hidden;
    background: var(--backdrop);
  }
  .canvas {
    position: relative;
    width: 1200px;
    height: 800px;
  }
  .business-card {
    position: absolute;
    left: 180px;
    top: 160px;
    width: 840px;
    height: 480px;
    border-radius: 16px;
    overflow: hidden;
    background: var(--card-white);
    box-shadow: 0 10px 30px rgba(40, 90, 50, 0.18);
  }
  .card-waves {
    position: absolute;
    inset: 0;
    width: 840px;
    height: 480px;
  }
  .identity {
    position: absolute;
    left: 64px;
    top: 96px;
  }
  .person-name {
    margin: 0;
    font-family: "Montserrat", sans-serif;
    font-weight: 700;
    font-size: 27px;
    letter-spacing: 0.5px;
    color: var(--text-green);
  }
  .person-role {
    margin: 4px 0 0;
    font-family: "Questrial", sans-serif;
    font-size: 21px;
    color: var(--text-green);
  }
  .brand {
    position: absolute;
    right: 48px;
    top: 120px;
    width: 300px;
    display: flex;
    flex-direction: column;
    align-items: center;
    gap: 10px;
  }
  .brand-mark {
    display: flex;
    align-items: center;
    gap: 14px;
  }
  .brand-dot {
    width: 30px;
    height: 30px;
    border-radius: 50%;
    background: var(--green-mid);
  }
  .brand-name {
    font-family: "Questrial", sans-serif;
    font-size: 40px;
    color: var(--text-green);
  }
  .brand-tagline {
    margin: 0;
    font-family: "Questrial", sans-serif;
    font-size: 14px;
    line-height: 1.4;
    text-align: center;
    color: var(--text-green);
  }
  .contact-list {
    position: absolute;
    left: 88px;
    top: 362px;
    margin: 0;
    padding: 0;
    list-style: none;
    font-family: "Questrial", sans-serif;
    font-size: 19px;
    color: var(--text-white);
  }
  .contact-item {
    display: flex;
    align-items: center;
    gap: 14px;
    height: 29px;
  }
  .contact-icon {
    width: 20px;
    height: 20px;
    flex: none;
  }
</style>
</head>
<body>
<main class="canvas">
  <section class="business-card" aria-label="Leaf Haven business card">
    <svg class="card-waves" viewBox="0 0 840 480" aria-hidden="true">
      <defs>
        <linearGradient id="waveFill" x1="0" y1="0" x2="1" y2="0">
          <stop offset="0" stop-color="var(--green-deep)"/>
          <stop offset="0.55" stop-color="var(--green-mid)"/>
          <stop offset="1" stop-color="var(--green-light)"/>
        </linearGradient>
      </defs>
      <path class="wave-stripe" d="M0,240 C180,206 360,244 500,312 C620,370 740,372 840,350 L840,355 C740,380 620,380 500,326 C360,258 180,222 0,256 Z" fill="url(#waveFill)"/>
      <path class="wave-band" d="M0,275 C180,242 360,284 500,352 C620,410 740,404 840,372 L840,480 L0,480 Z" fill="url(#waveFill)"/>
    </svg>

    <div class="identity">
      <h1 class="person-name">MIRA CALLAWAY</h1>
      <p class="person-role">General Manager</p>
    </div>

    <div class="brand">
      <div class="brand-mark">
        <span class="brand-dot" aria-hidden="true"></span>
        <span class="brand-name">Leaf Haven</span>
      </div>
      <p class="brand-tagline">Natural &amp; Organic Eco Products Online<br>Pantry · Superfoods · Skincare · Household</p>
    </div>

    <ul class="contact-list">
      <li class="contact-item">
        <svg class="contact-icon" viewBox="0 0 20 20" aria-hidden="true">
          <rect width="20" height="20" rx="4" fill="#fff"/>
          <path d="M6 4.5 L8.3 4.5 L9 7.5 L7.6 8.6 C8.3 10.2 9.6 11.6 11.3 12.4 L12.4 11 L15.5 11.7 L15.5 14 C15.5 14.8 14.8 15.5 14 15.5 C8.5 15.2 4.8 11.5 4.5 6 C4.5 5.2 5.2 4.5 6 4.5 Z" fill="var(--green-deep)"/>
        </svg>
        <span>+41780004512</span>
      </li>
      <li class="contact-item">
        <svg class="contact-icon" viewBox="0 0 20 20" aria-hidden="true">
          <rect width="20" height="20" rx="4" fill="#fff"/>
          <rect x="4" y="6" width="12" height="8.5" rx="1" fill="none" stroke="var(--green-deep)" stroke-width="1.5"/>
          <path d="M4.5 6.5 L10 11 L15.5 6.5" fill="none" stroke="var(--green-deep)" stroke-width="1.5"/>
        </svg>
        <span>mira@leafhaven-demo.com.au</span>
      </li>
      <li class="contact-item">
        <svg class="contact-icon" viewBox="0 0 20 20" aria-hidden="true">
          <rect width="20" height="20" rx="4" fill="#fff"/>
          <circle cx="10" cy="10" r="6" fill="none" stroke="var(--green-deep)" stroke-width="1.3"/>
          <ellipse cx="10" cy="10" rx="2.6" ry="6" fill="none" stroke="var(--green-deep)" stroke-width="1.2"/>
          <path d="M4 10 H16 M5 7 H15 M5 13 H15" stroke="var(--green-deep)" stroke-width="1.1"/>
        </svg>
        <span>www.leafhaven-demo.com.au</span>
      </li>
    </ul>
  </section>
</main>
</body>
</html>
```